Waterjet Cutting Business requires an up to date website

We currently have a website which is outdated and in need of modernization.
We are only looking for a simple website with around 4 pages: Home, Contact Us, Materials, Gallery.
We have some pictures and a logo which can be used.
Our primary business is profile cutting of materials to customers specifications using high-pressure water with abrasive.
We are looking for creative ideas and are open to suggestions!
http://brightfordcutworks.com/index.asp?pid=1
Update:
Cut quality picture (uploaded)
Map
Comparison to other profile cutting methods such as plasma/laser
Single page style without continuous scrolling
"We can cut virtually any material from any drawing whether it be a Full 3D cad models to hand sketched "
Target Market(s)
Film Industry, Prototype, Engineering, Architect, Artisits, one off designs
Industry/Entity Type
Engineering
Number of Pages Required
1 page
Font styles to use
Look and feel

```html
<!DOCTYPE html>
<html lang="en">
<head>
<meta charset="utf-8">
<title>Brightford Cutworks – Waterjet Profile Cutting</title>
<link href="https://fonts.googleapis.com/css2?family=Orbitron:wght@700&family=Arimo:wght@400;700&display=swap" rel="stylesheet">
<style>
:root{
  --brand:#1c5d8c;
  --brand-dark:#154b72;
  --panel:#f1f1f1;
  --text:#444;
  --muted:#777;
  --footer:#3b3d40;
  --field:#4f86ad;
  --submit:#3c4a55;
  --white:#fff;
}
*{box-sizing:border-box;margin:0;padding:0}
html,body{width:1200px;height:3509px;overflow:hidden}
body{position:relative;background:var(--white);font-family:"Arimo",Arial,sans-serif;color:var(--text)}
a{text-decoration:none}
.abs{position:absolute}
.display{font-family:"Orbitron",sans-serif;font-weight:700;color:var(--brand);text-transform:uppercase;letter-spacing:2px}
.rule{position:absolute;height:3px;width:70px;background:var(--brand);left:565px}
.copy{font-size:11.5px;line-height:18px;color:var(--muted);text-align:center}

/* header */
.site-header{left:0;top:0;width:1200px;height:105px;background:var(--white)}
.brand-name{left:164px;top:26px;display:flex;align-items:center;gap:12px;font-family:"Orbitron",sans-serif;font-weight:700;font-size:21px;color:var(--brand);letter-spacing:1px}
.brand-name i{width:20px;height:20px;background:var(--brand);display:block}
.phone-tab{left:808px;top:0;width:392px;height:33px;background:#e6e6e6;border-radius:0 0 0 18px;font-size:17px;font-weight:700;color:var(--brand);letter-spacing:1.5px;display:flex;align-items:center;padding-left:30px;gap:14px}
.phone-tab svg{width:22px;height:22px}
.main-nav{top:60px;left:0;width:1200px;height:20px}
.main-nav a{position:absolute;font-family:"Orbitron",sans-serif;font-weight:700;font-size:12px;color:var(--brand-dark);letter-spacing:1px}

/* hero */
.hero{left:0;top:105px;width:1200px;height:503px;display:flex}
.hero .shot{flex:1;height:100%}
.hero-caption{left:420px;top:492px;width:368px;font-size:21px;line-height:27px;font-weight:700;color:var(--white);text-align:center;letter-spacing:.3px}
.hero-arrow{top:338px;width:22px;height:22px;background:#333;display:flex;align-items:center;justify-content:center}

/* section titles */
.section-title{left:0;width:1200px;text-align:center;font-size:20px}

/* about */
.about-title{top:650px}
.about-copy{left:182px;top:716px;width:840px}

/* materials */
.materials{left:0;top:863px;width:1200px;height:412px;background:var(--panel)}
.materials .shot{left:0;top:0;width:461px;height:412px;background:linear-gradient(135deg,#2c4a52,#0f1c22 55%,#3b6b6d)}
.materials h2{left:491px;top:58px;font-size:20px}
.materials .rule{left:491px;top:92px}
.materials .body{left:491px;top:125px;width:680px;font-size:11.5px;line-height:17.5px;color:#666}
.materials .lead{font-weight:700;color:#555;margin-bottom:9px}
.materials p{margin-bottom:9px}
.materials .call{font-weight:700;color:var(--brand)}

/* cut quality */
.quality-title{top:1330px}
.quality-copy{left:170px;top:1394px;width:860px}
.compare-note{left:0;top:1442px;width:1200px;text-align:center;font-size:11.5px;font-weight:700;color:#555}
.samples{left:160px;top:1470px;width:878px;display:flex;gap:2px}
.sample{width:174px}
.sample .shot{height:245px;background:linear-gradient(90deg,#8d8d8b,#c4c4c1 40%,#9b9b98 70%,#b8b8b5)}
.sample h3{font-size:14px;color:#333;text-align:center;margin-top:12px;font-weight:700}
.sample small{display:block;text-align:center;font-size:11px;line-height:15px;color:#444;margin-top:2px}
.btn{display:flex;align-items:center;justify-content:center;font-family:"Orbitron",sans-serif;font-weight:700;color:var(--white);background:var(--brand);letter-spacing:2px;text-transform:uppercase}
.contact-btn{left:473px;top:1814px;width:255px;height:35px;font-size:13px}

/* video */
.video-band{left:0;top:1914px;width:1200px;height:297px;background:linear-gradient(180deg,#3f5f7a,#2b4a66 60%,#5a7186)}
.video-title{top:1956px;color:var(--white)}
.video-band-rule{left:565px;top:1992px;background:var(--white)}
.video-sub{left:0;top:2042px;width:1200px;text-align:center;font-size:14px;font-weight:700;color:var(--white)}
.video-frame{left:218px;top:2097px;width:755px;height:404px;border:2px solid var(--brand);background:var(--white);padding:7px}
.video-frame .shot{width:100%;height:100%;background:radial-gradient(circle at 50% 45%,#c9dced,#5f87ad 50%,#1f3c5c)}
.play{left:582px;top:2271px;width:36px;height:36px}

/* gallery */
.gallery-title{top:2556px}
.gallery-grid{left:164px;top:2644px;width:873px;height:414px;display:grid;grid-template-columns:repeat(3,1fr);grid-template-rows:repeat(2,1fr);gap:2px}
.tile{position:relative}
.tile.feature{background:linear-gradient(180deg,#2b6e99,#1d5579);color:var(--white);text-align:center;padding:56px 26px 0}
.tile.feature h3{font-size:16px;margin-bottom:8px}
.tile.feature p{font-size:10.5px;line-height:14px}
.gal-arrow{top:2818px;width:26px;height:70px}

/* contact */
.contact{left:0;top:3119px;width:1200px;height:344px;background:var(--brand)}
.contact h2{left:164px;top:54px;font-size:20px;color:var(--white)}
.contact .rule{left:386px;top:64px;width:46px;height:2px;background:var(--white)}
.info{left:164px;color:var(--white);font-size:13px;line-height:17px;display:flex;gap:14px}
.info svg{width:16px;height:16px;flex:none;margin-top:1px}
.info strong{font-size:14px}
.field{background:var(--field);color:#dfeaf3;font-size:12px;padding:8px 12px;position:absolute}
.submit{left:639px;top:262px;width:114px;height:35px;font-size:12px;background:var(--submit)}

.site-footer{left:0;top:3463px;width:1200px;height:46px;background:var(--footer);color:#ddd;font-size:12px}
.site-footer .legal{left:164px;top:16px}
.site-footer .brand-small{right:164px;top:15px;font-family:"Orbitron",sans-serif;font-weight:700;font-size:14px;color:var(--white);letter-spacing:1px}
</style>
</head>
<body>

<header class="abs site-header">
  <div class="abs brand-name"><i></i>Brightford Cutworks</div>
  <div class="abs phone-tab">
    <svg viewBox="0 0 24 24"><circle cx="12" cy="12" r="12" fill="#1c5d8c"/><path d="M8 6.5l2 2.3-1.2 1.5a8 8 0 004.9 4.9l1.5-1.2 2.3 2-1.4 1.9c-4.6-.3-9-4.7-9.3-9.3z" fill="#fff"/></svg>
    01632 960418
  </div>
  <nav class="abs main-nav">
    <a href="#" style="left:580px">HOME</a>
    <a href="#" style="left:667px">MATERIALS</a>
    <a href="#" style="left:803px">GALLERY</a>
    <a href="#" style="left:922px">CONTACT US</a>
  </nav>
</header>

<section class="abs hero">
  <div class="shot" role="img" aria-label="Waterjet cutting head working over a steel grid" style="background:linear-gradient(160deg,#9aa3ab,#2c3338 50%,#6d7a82)"></div>
  <div class="shot" role="img" aria-label="Waterjet machine lit in magenta light" style="background:linear-gradient(170deg,#2a1a3c,#b0307f 45%,#4b1b50 80%,#1a1326)"></div>
  <div class="shot" role="img" aria-label="Close-up of a blue waterjet cutting head" style="background:linear-gradient(150deg,#1d3c77,#4d6fa8 45%,#0f1d3c)"></div>
</section>
<p class="abs hero-caption">We can cut virtually any material from any drawing whether it be a Full 3D cad models to hand sketched</p>
<div class="abs hero-arrow" style="left:4px"><svg width="10" height="10" viewBox="0 0 10 10"><path d="M7 1L3 5l4 4" stroke="#fff" stroke-width="2" fill="none"/></svg></div>
<div class="abs hero-arrow" style="left:1174px"><svg width="10" height="10" viewBox="0 0 10 10"><path d="M3 1l4 4-4 4" stroke="#fff" stroke-width="2" fill="none"/></svg></div>

<h2 class="abs display section-title about-title">About Brightford Cutworks</h2>
<div class="rule" style="top:684px"></div>
<p class="abs copy about-copy">Lorem ipsum dolor sit amet, consectetuer adipiscing elit, sed diam nonummy nibh euismod tincidunt ut laoreet dolore magna aliquam erat volutpat. Ut wisi enim ad minim veniam, quis nostrud exerci tation ullamcorper suscipit lobortis nisl ut aliquip ex ea commodo consequat. Duis autem vel eum iriure dolor in hendrerit in vulputate velit esse molestie consequat, vel illum dolore eu feugiat nulla facilisis at vero eros et accumsan nonummy nibh euismod tincidunt ut laoreet dolore magna aliquam erat volutpat. Ut wisi enim ad minim veniam, quis nostrud exerci tation ullamcorper suscipit lobortis nisl ut aliquip ex ea commodo consequat. Duis autem et iusto odio dignissim qui blandit praesent luptatum zzril delenit augue duis dolore te feugait nulla facilisi.</p>

<section class="abs materials">
  <div class="abs shot" role="img" aria-label="Waterjet machine head with blue hoses in a workshop"></div>
  <h2 class="abs display">Materials</h2>
  <div class="rule"></div>
  <div class="abs body">
    <p class="lead">It is possible to cut virtually any profile in any material with waterjet</p>
    <p>Materials we can cut include, but are not limited to, all metals &amp; alloys, stone &amp; ceramics, composites, solid surface, wood, glass, acrylics, resins, silicones, plastics, foams, carpet and felts. We can also cut laminated dissimilar materials which can often be very hard to cut using conventional methods. We are always happy to test cut a sample of your material free of charge to demonstrate the quality of cut achievable.</p>
    <p>Employing Vantor's low pressure vacuum assist we can pierce and cut brittle materials such as acrylics and ceramics. In addition Adaptive Jet technology with Precision Taper Control produces more accurate parts at significantly higher cutting speeds than parts cut with a conventional waterjet.</p>
    <p class="call">If you are not sure whether waterjet cutting will fulfill your requirements give us a call.</p>
  </div>
</section>

<h2 class="abs display section-title quality-title">Cut Quality Methods</h2>
<div class="rule" style="top:1364px"></div>
<p class="abs copy quality-copy">Lorem ipsum dolor sit amet, consectetuer adipiscing elit, sed diam nonummy nibh euismod tincidunt ut laoreet dolore magna aliquam erat volutpat. Ut wisi enim ad minim veniam, quis nostrud exerci tation ullamcorper suscipit lobortis nisl ut aliquip ex ea commodo consequat.</p>
<p class="abs compare-note">Comparison to other profile cutting methods such as plasma/laser</p>
<div class="abs samples">
  <div class="sample"><div class="shot" role="img" aria-label="Q1 cut surface sample"></div><h3>Separation Cut</h3></div>
  <div class="sample"><div class="shot" role="img" aria-label="Q2 cut surface sample"></div><h3>Through Cut</h3></div>
  <div class="sample"><div class="shot" role="img" aria-label="Q3 cut surface sample"></div><h3>Clean Cut</h3><small>Typicaly Closer<br>than +/- 0.010"</small></div>
  <div class="sample"><div class="shot" role="img" aria-label="Q4 cut surface sample"></div><h3>Good Edge Finish</h3></div>
  <div class="sample"><div class="shot" role="img" aria-label="Q5 cut surface sample"></div><h3>Excellent Edge Finish</h3><small>Typicaly Closer<br>than +/- 0.005"</small></div>
</div>
<a class="abs btn contact-btn" href="#">Contact Us Today</a>

<section class="abs video-band" role="img" aria-label="Faded view of a historic stone manor in blue tint"></section>
<h2 class="abs display section-title video-title">Watch Video</h2>
<div class="rule video-band-rule"></div>
<p class="abs video-sub">Technology we use &amp; watch video to check our process how we work</p>
<div class="abs video-frame"><div class="shot" role="img" aria-label="Waterjet nozzle cutting through a plate under water spray"></div></div>
<svg class="abs play" viewBox="0 0 36 36"><circle cx="18" cy="18" r="18" fill="rgba(255,255,255,.55)"/><path d="M14 11l11 7-11 7z" fill="#555"/></svg>

<h2 class="abs display section-title gallery-title">Work Gallery</h2>
<div class="rule" style="top:2592px"></div>
<svg class="abs gal-arrow" style="left:108px" viewBox="0 0 26 70"><path d="M22 2L4 35l18 33" stroke="#ccc" stroke-width="2" fill="none"/></svg>
<svg class="abs gal-arrow" style="left:1064px" viewBox="0 0 26 70"><path d="M4 2l18 33L4 68" stroke="#ccc" stroke-width="2" fill="none"/></svg>
<div class="abs gallery-grid">
  <div class="tile" role="img" aria-label="Cutting head throwing sparks" style="background:linear-gradient(160deg,#6d6e6b,#2b2a28 60%,#8a7d70)"></div>
  <div class="tile feature"><h3>Lorem Ipsum</h3><p>Lorem ipsum dolor sit amet, consectetuer adipiscing elit, sed diam nonummy nibh euismod tincidunt ut laoreet dolore magna aliquam erat volutpat. Ut wisi enim ad minim veniam, quis nostrud exerci.</p></div>
  <div class="tile" role="img" aria-label="Machine head under teal light" style="background:linear-gradient(150deg,#0e1a1c,#2e8378 50%,#0b1213)"></div>
  <div class="tile" role="img" aria-label="Waterjet head with blue hoses" style="background:linear-gradient(150deg,#12263a,#3d6d8c 50%,#0c1722)"></div>
  <div class="tile" role="img" aria-label="Cutting table lit in green" style="background:linear-gradient(160deg,#0b2612,#2fb34a 50%,#0a1f0e)"></div>
  <div class="tile" role="img" aria-label="Machine lit in magenta" style="background:linear-gradient(160deg,#2a1230,#c23a9a 50%,#3a1640)"></div>
</div>

<section class="abs contact">
  <h2 class="abs display">Contact Us</h2>
  <div class="abs rule"></div>
  <div class="abs info" style="top:100px">
    <svg viewBox="0 0 16 16"><path d="M8 0a5.5 5.5 0 00-5.5 5.5C2.5 10 8 16 8 16s5.5-6 5.5-10.5A5.5 5.5 0 008 0zm0 7.7a2.2 2.2 0 110-4.4 2.2 2.2 0 010 4.4z" fill="#fff"/></svg>
    <div><strong>Brightford Cutworks</strong><br>Unit 7, Kestrel Court, Marlow Lane,<br>Ashgrove Trade Park, Fenbridge<br>Wessex, FB4 2QT</div>
  </div>
  <div class="abs info" style="top:196px">
    <svg viewBox="0 0 16 16"><path d="M3 1l3 3-1.6 2a9 9 0 005.6 5.6L12 10l3 3-2 2.5C7 15 1 9 .5 3z" fill="#fff"/></svg>
    <div>01632 960418.</div>
  </div>
  <div class="abs info" style="top:235px">
    <svg viewBox="0 0 16 16"><rect x="1" y="3" width="14" height="10" fill="#fff"/><path d="M1 3l7 6 7-6" stroke="#1c5d8c" stroke-width="1.4" fill="none"/></svg>
    <div>info@brightfordcutworks.com</div>
  </div>
  <div class="field" style="left:639px;top:47px;width:398px;height:33px">Name</div>
  <div class="field" style="left:639px;top:89px;width:193px;height:35px">Email</div>
  <div class="field" style="left:842px;top:89px;width:195px;height:35px">Mobile</div>
  <div class="field" style="left:639px;top:136px;width:398px;height:108px">Message</div>
  <a class="abs btn submit" href="#">Submit</a>
</section>

<footer class="abs site-footer">
  <p class="abs legal">Copyright © 2018 Brightford Cutworks &nbsp;|&nbsp; All Rights Reserved.</p>
  <div class="abs brand-small">BRIGHTFORD CUTWORKS</div>
</footer>

</body>
</html>
```